Business card design needed

Mechanical services (heavy)
Training needs
Air conditioning (Automotive)
Parts Supplier

Industry/Entity Type

Automotive

Contact Information for Business Card

R T Mechanical Services
Colin Harwood (director)
47 Marlow Ridge highway
North Kelbrook W.A 6218
Mobile: 0417 563 904
rtmechanical4@mailvex.com

```html
<!DOCTYPE html>
<html lang="en">
<head>
<meta charset="utf-8">
<title>R T Mechanical Services – Business Card</title>
<link rel="stylesheet" href="https://fonts.googleapis.com/css2?family=Archivo+Black&family=Open+Sans:wght@300;400&display=swap">
<style>
  :root {
    --page: #d6d6d6;
    --card: #232323;
    --card-light: #3a3a3a;
    --band: #141414;
    --red: #e0312c;
    --blue: #2f86d6;
    --text-soft: #cfcfcf;
    --divider: #555555;
  }
  * { margin: 0; padding: 0; box-sizing: border-box; }
  html, body {
    width: 831px; height: 1200px; overflow: hidden;
    background: var(--page);
  }
  .card {
    position: absolute; left: 65px;
    width: 700px; height: 400px;
    border-radius: 6px; overflow: hidden;
    box-shadow: 0 10px 28px rgba(0,0,0,.35);
  }
  .card-front {
    top: 150px;
    background: radial-gradient(ellipse at 50% 42%, #555 0%, #333 30%, var(--card) 65%, #1a1a1a 100%);
  }
  .card-back {
    top: 650px;
    background: linear-gradient(160deg, var(--card-light) 0%, var(--card) 55%, #1c1c1c 100%);
  }
  .brand {
    position: absolute; left: 0; right: 0; top: 150px;
    display: flex; align-items: center; justify-content: center; gap: 16px;
  }
  .brand-dot {
    width: 56px; height: 56px; border-radius: 50%;
    background: #8a8a8a;
  }
  .brand-name {
    font-family: "Archivo Black", sans-serif;
    font-size: 40px; color: var(--blue); letter-spacing: 1px;
  }
  .services {
    position: absolute; left: 50px; top: 120px;
    list-style: none;
    font-family: "Open Sans", sans-serif; font-weight: 300;
    font-size: 19px; line-height: 27px; color: var(--text-soft);
  }
  .divider {
    position: absolute; left: 355px; top: 80px;
    width: 1px; height: 80px; background: var(--divider);
  }
  .holder { position: absolute; left: 380px; top: 82px; }
  .holder-name {
    font-family: "Archivo Black", sans-serif;
    font-size: 30px; color: var(--red); line-height: 1.1;
  }
  .holder-role {
    font-family: "Archivo Black", sans-serif;
    font-size: 16px; color: var(--blue); letter-spacing: 1px;
  }
  .contact {
    position: absolute; left: 470px; top: 248px;
    list-style: none;
    font-family: "Open Sans", sans-serif; font-size: 14px;
    color: var(--red); line-height: 24px;
  }
  .contact li { display: flex; align-items: center; gap: 10px; }
  .contact svg { width: 16px; height: 16px; }
  .address-band {
    position: absolute; left: 0; bottom: 0;
    width: 100%; height: 72px; background: var(--band);
    display: flex; align-items: center; gap: 14px; padding-left: 40px;
  }
  .address-band svg { width: 16px; height: 22px; }
  .address {
    font-family: "Open Sans", sans-serif; font-style: normal;
    font-size: 15px; line-height: 21px; color: var(--red);
  }
</style>
</head>
<body>
  <section class="card card-front" aria-label="Card front">
    <div class="brand">
      <span class="brand-dot"></span>
      <span class="brand-name">R T MECHANICAL</span>
    </div>
  </section>

  <section class="card card-back" aria-label="Card back">
    <ul class="services">
      <li>Mechanical services (heavy)</li>
      <li>Training needs</li>
      <li>Air conditioning (Automotive)</li>
      <li>Parts Supplier</li>
    </ul>
    <div class="divider"></div>
    <div class="holder">
      <div class="holder-name">Colin Harwood</div>
      <div class="holder-role">DIRECTOR</div>
    </div>
    <ul class="contact">
      <li>
        <svg viewBox="0 0 16 16" aria-hidden="true"><path d="M3 1.5l3 3-1.6 1.8c.8 1.8 2.3 3.3 4.3 4.3L10.5 9l3 3-2 2C6 14 2 10 2 3.5z" fill="none" stroke="var(--blue)" stroke-width="1.4" stroke-linejoin="round"/></svg>
        0417 563 904
      </li>
      <li>
        <svg viewBox="0 0 16 16" aria-hidden="true"><rect x="1.5" y="3.5" width="13" height="9" fill="none" stroke="var(--blue)" stroke-width="1.4"/><path d="M1.5 3.5L8 9l6.5-5.5" fill="none" stroke="var(--blue)" stroke-width="1.4"/></svg>
        rtmechanical4@mailvex.com
      </li>
    </ul>
    <div class="address-band">
      <svg viewBox="0 0 16 22" aria-hidden="true"><path d="M8 1a6 6 0 0 1 6 6c0 4.5-6 13-6 13S2 11.5 2 7a6 6 0 0 1 6-6z" fill="var(--blue)"/><circle cx="8" cy="7" r="2.3" fill="var(--band)"/></svg>
      <address class="address">R T Mechanical Services, 47 Marlow Ridge<br>highway North Kelbrook W.A 6218</address>
    </div>
  </section>
</body>
</html>
```